Classy, Elegant, Simple Business Card Design

Looking to have a classy, simple, and elegant design. Want a top notch designed business card. I really like the look of the new brivo credit card. I also like the design I attached. I am trying to reach 21-29 year old females for booking us for there wedding or event. We offer Disc Jockey Service, Photo Booth Rentals, and Uplighting .

Target Market(s)

21-28 year old females

Contact Information for Business Card

Has to have logo, website, email, and phone number

Font styles to use
Other font styles liked:
• open to font choice, modern, clean
Designer to choose
33a6d7
0791cd
0555a3
ffffff

Requirements
Must have
• Has to have logo, website, email, and phone number
Nice to have
• I really like the design of the new brivo credit card. I also included my logo and some designs I like
Should not have
• clutter or too much info

```html
<!DOCTYPE html>
<html lang="en">
<head>
<meta charset="utf-8">
<title>Tidewell Business Card</title>
<link rel="stylesheet" href="https://fonts.googleapis.com/css2?family=Inter:wght@400&family=Mulish:wght@400;600&display=swap">
<style>
  :root {
    --stage: #000000;
    --label: #ffffff;
    --sky: #33a6d7;
    --azure: #0791cd;
    --navy: #0555a3;
    --white: #ffffff;
    --mist: #8fb0d6;
    --ice: #86cbea;
  }
  * { margin: 0; padding: 0; box-sizing: border-box; }
  html, body {
    width: 1200px; height: 1200px; overflow: hidden;
    background: var(--stage);
  }
  .canvas { position: relative; width: 1200px; height: 1200px; }
  .side-label {
    position: absolute;
    font-family: "Inter", Helvetica, Arial, sans-serif;
    font-size: 38px; line-height: 1; color: var(--label);
  }
  .side-label--front { left: 119px; top: 172px; }
  .side-label--back { left: 994px; top: 597px; width: 84px; text-align: right; }
  .card {
    position: absolute; width: 638px; height: 354px;
    border-radius: 16px; overflow: hidden;
  }
  .card--front { left: 122px; top: 245px; }
  .card--back { left: 440px; top: 670px; }
  .card__bg { position: absolute; inset: 0; width: 100%; height: 100%; display: block; }
  .card__text {
    position: absolute;
    font-family: "Mulish", "Avenir", sans-serif;
    color: var(--white); white-space: nowrap;
  }
  .contact { left: 70px; top: 90px; font-size: 14.5px; line-height: 22px; letter-spacing: 0.2px; }
  .website { left: 70px; top: 254px; font-size: 16px; letter-spacing: 0.4px; }
  .brand-name {
    left: 412px; top: 238px; width: 160px; text-align: center;
    font-size: 30px; font-weight: 600; color: var(--navy); letter-spacing: 0.5px;
  }
</style>
</head>
<body>
<main class="canvas">
  <div class="side-label side-label--front">Front</div>

  <section class="card card--front">
    <svg class="card__bg" viewBox="0 0 638 354" aria-hidden="true">
      <defs>
        <linearGradient id="front-sweep" x1="0" y1="260" x2="560" y2="0" gradientUnits="userSpaceOnUse">
          <stop offset="0" stop-color="#0791cd"/>
          <stop offset="0.38" stop-color="#0784c6"/>
          <stop offset="0.6" stop-color="#0555a3"/>
          <stop offset="0.78" stop-color="#5589c2"/>
          <stop offset="1" stop-color="#8fb0d6"/>
        </linearGradient>
        <linearGradient id="front-top" x1="0" y1="0" x2="0" y2="120" gradientUnits="userSpaceOnUse">
          <stop offset="0" stop-color="#0555a3" stop-opacity="0.35"/>
          <stop offset="1" stop-color="#0555a3" stop-opacity="0"/>
        </linearGradient>
        <linearGradient id="front-glow" x1="0" y1="275" x2="-18" y2="150" gradientUnits="userSpaceOnUse">
          <stop offset="0" stop-color="#ffffff"/>
          <stop offset="0.25" stop-color="#e4f3fb"/>
          <stop offset="1" stop-color="#0791cd" stop-opacity="0"/>
        </linearGradient>
      </defs>
      <rect width="638" height="354" fill="url(#front-sweep)"/>
      <rect width="638" height="120" fill="url(#front-top)"/>
      <polygon points="0,273 638,354 0,130" fill="url(#front-glow)"/>
      <polygon points="0,274 638,354 0,354" fill="#3aaadb"/>
    </svg>
    <div class="card__text contact">
      <div>T. +123 456 7890</div>
      <div>contact@tidewell.com</div>
    </div>
  </section>

  <div class="side-label side-label--back">Back</div>

  <section class="card card--back">
    <svg class="card__bg" viewBox="0 0 638 354" aria-hidden="true">
      <defs>
        <linearGradient id="back-base" x1="0" y1="354" x2="638" y2="120" gradientUnits="userSpaceOnUse">
          <stop offset="0" stop-color="#0555a3"/>
          <stop offset="0.45" stop-color="#0791cd"/>
          <stop offset="1" stop-color="#86cbea"/>
        </linearGradient>
        <linearGradient id="back-glow" x1="0" y1="0" x2="-60" y2="170" gradientUnits="userSpaceOnUse">
          <stop offset="0" stop-color="#ffffff"/>
          <stop offset="0.2" stop-color="#dff1fa"/>
          <stop offset="1" stop-color="#0791cd" stop-opacity="0"/>
        </linearGradient>
        <linearGradient id="back-upper" x1="0" y1="0" x2="638" y2="0" gradientUnits="userSpaceOnUse">
          <stop offset="0" stop-color="#33a6d7"/>
          <stop offset="1" stop-color="#86cbea"/>
        </linearGradient>
        <linearGradient id="back-corner" x1="638" y1="200" x2="450" y2="354" gradientUnits="userSpaceOnUse">
          <stop offset="0" stop-color="#ffffff" stop-opacity="0.85"/>
          <stop offset="1" stop-color="#ffffff" stop-opacity="0"/>
        </linearGradient>
      </defs>
      <rect width="638" height="354" fill="url(#back-base)"/>
      <polygon points="0,0 638,190 638,354 0,354" fill="url(#back-glow)"/>
      <polygon points="638,190 638,354 430,354" fill="url(#back-corner)"/>
      <polygon points="0,0 638,0 638,190" fill="url(#back-upper)"/>
    </svg>
    <div class="card__text website">tidewell.com</div>
    <div class="card__text brand-name">Tidewell</div>
  </section>
</main>
</body>
</html>
```